website design + images

We need a very appealing website design, layout and images for a sales analytics and sales productivity services company based in San Ramon, California. We need a good design for the home page and a template for all other pages (total 2 designs), and images for all inner pages (center column/banner images, and right hand top corner small images). There are about 18 inner pages.
Updates

Our existing website is www.corvexa.com
Our corporate colours are the ones that are there on the website. The logo is also shown. We will be changing the tagline to "accelerating revenue" or equivalent of that.

Please use the document "website for corvexa - template v2.doc" that I just uploaded for any reference to the content, navigation and wireframes. A few more clarifications are provided mainly for the link "Solutions".

Hemant Loravi

Hi,
We just uploaded ver 4 of the website template. There is more elaboration provided around the sublinks / sections for Solutions. Pls review and do get back if you need any clarifications.

Rgds
Hemant Loravi

Hi all,
We have so far received a few good designs. The designs are more or less on the right track. I would like to urge all of you to use the content and navigation provided in the document attached to our brief "website for corvexa - template v4.doc".  Please DO NOT use the content in our existing website www.corvexa.com . That is very old. We mentioned it only for reference to colour theme and broad details.

We have totally 13 sections in Solutions pages. They may be designed as a tree of links - first level sublinks - second level sublinks or links - first level sublinks and the remaining as sections within the first level sublinks pages. The page design would remain the same for all inner pages except careers. But after finalizing the design for the inner page, we will need images for the different inner pages.

Rgds
Hemant Loravi

Hi,
Thank you all for participation and very good designs. We are quite happy with what we have seen. We have now shortlisted about 4 vendors and sending invididual feedback to them for further improvement. We will be finalizing by Monday or Tuesday.  To the vendors who do not get feedback from us, thank you very much for participation. We may still do business in future for some of our other needs. 
The following are the process steps / expectations going forward, 
1. Feedback to the shortlisted designers and inviting improvements.
2. Review of the improved designs and further shortlist & feedback or direct finalization.
3. The design should be in 1024*768
2. Number of page designs = 2 (home page, inner page).
4. Home page design: instead of delivery model and customers, show one link "Why Us".
4. Solutions page design:  We will be needing an image in center column of solutions page that in a nutshell gives all the different types of solutions we provide. The entire set of solutions is in our attached document website for corvexa - template v4 and I am just uploading v5 with more description on sublinks.
5. After selection, we will be needing images for all the solution pages (total 12 pages under solutions + one solutions page), 1 image for Why Us?, 1 for Careers, and 3 for company (about us/ team, core values, ...) = total 18

Rgds
Hemant Loravi

Target Market(s)

We are a sales analytics and sales productivity services company. We help B2B companies with: sales planning; sales operations and sales measurement. The characteristics of our customers are:
- B2B medium enterprises (USD 100M- USD 2B in revenue) in the US
- Primary target verticals are: high-tech, engineering and professional services firms
- Our primary target customers titles are VP of Sales or VP of marketing; we could be selling to the CEO at companies with revenues below $200M

Industry/Entity Type

Consulting

Requirements
Must have
• - Clean, uncluttered design
• - Easy navigation; minimum clicks
Nice to have
• We have already built a content management system and wireframes for this site. To the extent possible, it would be great to leverage the wireframe structure we built, provided you don’t have to compromise on the look and feel and navigation of the site. Below is what we currently have as banner sizes and resolutions are:
• Home page banner size: 950 * 250’
• All pages – center top - image size: 558 * 160
• All pages – right hand top image – 175*135’

```html
<!DOCTYPE html>
<html lang="en">
<head>
<meta charset="utf-8">
<title>Corvexa</title>
<link href="https://fonts.googleapis.com/css2?family=Didact+Gothic&family=Noto+Sans:wght@400;700&family=Open+Sans:wght@600;700&display=swap" rel="stylesheet">
<style>
:root{
  --green:#2f8f2a;
  --green-dark:#1f6e1c;
  --green-light:#46b23a;
  --blue:#2f5fb3;
  --blue-nav:#3d7bd6;
  --sky:#2b8ee6;
  --sky-light:#8fcaf5;
  --ink:#111;
  --grey-bg:#f2f3f2;
  --white:#fff;
}
*{margin:0;padding:0;box-sizing:border-box}
html,body{width:1200px;height:982px;overflow:hidden}
body{position:relative;background:linear-gradient(#fff 0,#fff 560px,#f1f1f1 930px);font-family:"Noto Sans",sans-serif;color:var(--ink)}
.abs{position:absolute}

.topbar{left:0;top:0;width:1200px;height:39px;background:linear-gradient(#3aa032,var(--green-dark))}
.signin{left:698px;top:0;width:164px;height:44px;background:linear-gradient(#3f78d2,#2a57a8);border-radius:0 0 8px 8px;color:#fff;font:700 14px "Noto Sans",sans-serif;display:flex;align-items:center;justify-content:center;gap:6px}
.toplink{top:0;height:39px;display:flex;align-items:center;gap:7px;color:#fff;font:700 14px "Noto Sans",sans-serif}

.brand{left:74px;top:140px;font:400 40px/1 "Didact Gothic",sans-serif;color:var(--blue);letter-spacing:1px}

.nav-bar{left:418px;top:74px;width:707px;height:15px;background:var(--blue)}
.nav{right:75px;top:74px;list-style:none;text-align:right}
.nav li{height:23.5px;display:flex;justify-content:flex-end;align-items:center;gap:8px;font:700 14px "Open Sans",sans-serif;color:#111}
.nav li:nth-child(2){margin-top:4px}
.nav li::after{content:"";width:14px;height:14px;background:var(--blue-nav)}
.nav li.current{color:#fff;height:15px;font-size:13px;padding-right:22px}
.nav li.current::after{display:none}

.banner-frame{left:65px;top:222px;width:1072px;height:293px;background:#3a3a3a;box-shadow:0 4px 10px rgba(0,0,0,.35)}
.banner{left:82px;top:229px;width:1038px;height:279px;background:radial-gradient(ellipse at 30% 40%,var(--sky-light),var(--sky) 70%);overflow:hidden}
.banner-photo{right:0;top:0;width:483px;height:279px;background:linear-gradient(100deg,#4aa2e6,#cfd6dc 35%,#9aa3ab 70%,#e8ecef)}
.banner-strip{left:0;bottom:0;width:1038px;height:47px;background:rgba(255,255,255,.22)}
.banner h1{left:18px;top:62px;font:700 26px "Open Sans",sans-serif;color:#fff;letter-spacing:.5px}
.banner p{left:18px;top:109px;width:420px;font:600 13.5px/17px "Open Sans",sans-serif;color:#fff}
.btn-more{left:12px;top:169px;width:104px;height:28px;border-radius:14px;background:linear-gradient(var(--green-light),var(--green));color:#fff;font:600 12px "Open Sans",sans-serif;display:flex;align-items:center;padding-left:12px;gap:7px}
.dots{left:20px;top:244px;display:flex;gap:19px}
.dots span{width:22px;height:22px;border-radius:50%;background:#fff}
.dots span.active{background:radial-gradient(circle at 40% 35%,#6de05a,#1f9a1a)}

.welcome{left:76px;top:557px;width:300px}
.welcome h2{font:400 28px/32px "Didact Gothic",sans-serif;color:#111}
.welcome h2 span{display:block;font-size:34px;line-height:38px;color:var(--blue)}
.welcome p{margin-top:12px;font:400 14.5px/17px "Noto Sans",sans-serif}
.link-more{display:block;margin-top:15px;font:700 13.5px "Noto Sans",sans-serif;color:var(--green)}

.testi-head{left:75px;top:756px;width:303px;height:35px;background:linear-gradient(var(--green-light),var(--green));color:#fff;font:700 19px "Open Sans",sans-serif;padding-left:6px;display:flex;align-items:center}
.testi{left:75px;top:791px;width:303px;height:140px;background:var(--grey-bg)}
.quote{font:700 44px/1 Georgia,serif;color:var(--green-light)}
.testi p{left:38px;top:15px;width:250px;font:400 14.5px/17px "Noto Sans",sans-serif}
.testi .who{left:38px;top:102px;font:700 14.5px/17px "Noto Sans",sans-serif}

.card{top:560px;width:222px}
.card-img{height:136px;border:3px solid var(--green);background:linear-gradient(135deg,#f3f3f3,#b9bec3 60%,#6d7379)}
.card-body{height:160px;background:var(--grey-bg);padding:6px 9px}
.card h3{font:700 15.5px/20px "Open Sans",sans-serif;color:var(--green);letter-spacing:.3px}
.card p{margin-top:6px;font:400 12.7px/15.5px "Noto Sans",sans-serif}
.card-more{height:23px;background:var(--green);color:#fff;font:700 13.5px "Noto Sans",sans-serif;padding-left:10px;display:flex;align-items:center}

.footer{left:0;top:941px;width:1200px;height:41px;background:linear-gradient(#3aa032,var(--green-dark));color:#fff;font:700 14px "Noto Sans",sans-serif}
.footer .copy{left:77px;top:12px}
.footer .links{right:30px;top:12px;word-spacing:4px}
</style>
</head>
<body>
<header>
  <div class="abs topbar"></div>
  <div class="abs signin">
    <svg width="14" height="22" viewBox="0 0 14 22"><circle cx="7" cy="6" r="5" fill="#f3c230"/><rect x="5.5" y="10" width="3" height="11" fill="#f3c230"/><rect x="8" y="15" width="3" height="2" fill="#f3c230"/></svg>
    Sign in/Register
  </div>
  <div class="abs toplink" style="left:898px">
    <svg width="16" height="18" viewBox="0 0 16 18"><path d="M3 1l4 4-2 2c1 3 3 5 6 6l2-2 3 4-3 2C7 17 1 10 1 3z" fill="#8fd3f0"/></svg>
    Contact Us
  </div>
  <div class="abs toplink" style="left:1034px">
    <svg width="22" height="20" viewBox="0 0 22 20"><rect x="8" y="1" width="6" height="5" fill="#fff"/><rect x="1" y="13" width="6" height="5" fill="#fff"/><rect x="15" y="13" width="6" height="5" fill="#fff"/><path d="M11 6v4M4 13v-3h14v3" stroke="#fff" stroke-width="2" fill="none"/></svg>
    Sitemap
  </div>

  <div class="abs brand">CORVEXA</div>

  <div class="abs nav-bar"></div>
  <ul class="abs nav">
    <li class="current">HOME</li>
    <li>SOLUTIONS</li>
    <li>DELIVERY MODEL</li>
    <li>CUSTOMERS</li>
    <li>COMPANY</li>
    <li>CAREERS</li>
  </ul>
</header>

<section class="abs banner-frame"></section>
<section class="abs banner">
  <div class="abs banner-photo" role="img" aria-label="Photo of a smiling business team"></div>
  <div class="abs banner-strip"></div>
  <h1 class="abs">GAIN BUSINESS AGILITY.</h1>
  <p class="abs">With on-demand solutions, eliminate long development and implementation times.</p>
  <div class="abs btn-more"><span>›</span>Read more</div>
  <div class="abs dots"><span class="active"></span><span></span><span></span></div>
</section>

<section class="abs welcome">
  <h2>WELCOME TO<span>CORVEXA</span></h2>
  <p>Lorem Ipsum is simply dummy text of the printing and typesetting industry. Lorem Ipsum has been the industry's standard dummy text ever since the 1500s.</p>
  <span class="link-more">Read More</span>
</section>

<div class="abs testi-head">CUSTOMER TESTIMONIAL</div>
<section class="abs testi">
  <span class="abs quote" style="left:4px;top:8px">“</span>
  <p class="abs">There are many variations of passages of Lorem Ipsum available, but the majority have suffered alteration in some form.</p>
  <div class="abs who">Daniel K. Marsh<br>Director</div>
  <span class="abs quote" style="left:254px;top:98px">”</span>
</section>

<article class="abs card" style="left:434px">
  <div class="card-img" role="img" aria-label="Photo of a team meeting around a table with laptops"></div>
  <div class="card-body">
    <h3>SALES PLANNING<br>ANALYTICS</h3>
    <p>Lorem Ipsum is simply dummy text of the printing and typesetting industry. Lorem Ipsum has been the industry's dummy text ever since the 1500s.</p>
  </div>
  <div class="card-more">+Read More</div>
</article>
<article class="abs card" style="left:670px">
  <div class="card-img" role="img" aria-label="Photo of support staff wearing headsets"></div>
  <div class="card-body">
    <h3>SALES OPERATIONS<br>SUPPORT</h3>
    <p>Lorem Ipsum is simply dummy text of the printing and typesetting industry. Lorem Ipsum has been the industry's dummy text ever since the 1500s.</p>
  </div>
  <div class="card-more">+Read More</div>
</article>
<article class="abs card" style="left:906px">
  <div class="card-img" role="img" aria-label="Photo of hands reviewing printed charts"></div>
  <div class="card-body">
    <h3>SALES MEASUREMENT<br>ANALYTICS</h3>
    <p>Lorem Ipsum is simply dummy text of the printing and typesetting industry. Lorem Ipsum has been the industry's dummy text ever since the 1500s.</p>
  </div>
  <div class="card-more">+Read More</div>
</article>

<footer class="abs footer">
  <span class="abs copy">Copyright © Corvexa 2010. All rights reserved.</span>
  <span class="abs links">disclaimer | contact us</span>
</footer>
</body>
</html>
```